Flyer Design Project

To whom it may concern
Would love the benefit of your expertise

I have a project which is to increase business activity. There are dozens or real estate adds and I want mine to stand out from all others.

My strategy is going with a 50 % sale, what I need is something catchy and something that will make my brochure stand out from the other dozen brochure they have in the mail I need the WOW! Factor

DL Brochure (DL Brochures, Size 99 mm X 210 mm) atm the moment im thinking of only using 1 side but if your design needs both side that is an option

below will be the wording I'm thinking of going with the describe the sale and benefits, i am flexible with the wording if your think something else will sound better

***New Wording***

50% OFF COMMISSION
Sounds good doesn’t it?
Our promise to you from Harlow Real Estate

List your property with us
And if your buyer has not been found within 15 days
We will slash 50% off our commission!
You will have the benefit of Real Estate consultants
Derek Harlow and Anthony Velluti
With over 40 years combined experience
Working hard to find your buyer.

Call Today 0491 627 158

Condition Apply

Follow us on Facebook www.facebook.com/kelbrookhomes

I have attached the link to our website and Facebook page if you want to see a possible color scheme
but i am open to anything

http://keystonekelbrook.com.au/
http://www.facebook.com/kelbrookhomes

Good Luck !!!

Target Market(s)

Home Seller's

Industry/Entity Type

Real Estate

Requirements
Nice to have
• our logo but remember this flyer is not to market our self its to market our offer
so i want to 50% off the stand out not Keystone Harlow Real Estate
Should not have
• House in the Background, i would much rather the 50% take up half the page than have the house or even a quirky un related image

```html
<!DOCTYPE html>
<html lang="en">
<head>
<meta charset="utf-8">
<title>Harlow Real Estate – 50% Off Commission</title>
<link rel="stylesheet" href="https://fonts.googleapis.com/css2?family=Oswald:wght@200;300;500;600&family=Roboto+Condensed:wght@400;500&display=swap">
<style>
  :root {
    --sky-dark: #17302f;
    --sky-mid: #234a43;
    --umbrella-green: #2d7a45;
    --grass: #3f5f34;
    --paper: #ffffff;
    --ink: #3a3a3a;
    --brand-green: #1e6b39;
    --headline: #ffffff;
  }
  * { margin: 0; padding: 0; box-sizing: border-box; }
  html, body {
    width: 670px;
    height: 1200px;
    overflow: hidden;
    background: var(--paper);
  }
  .flyer {
    position: relative;
    width: 670px;
    height: 1200px;
    background: var(--paper);
    overflow: hidden;
  }
  .hero-scene {
    position: absolute;
    left: 0; top: 0;
    width: 670px;
    height: 720px;
    background:
      radial-gradient(ellipse 60% 35% at 18% 48%, rgba(60,150,80,0.75), rgba(60,150,80,0) 70%),
      radial-gradient(ellipse 55% 30% at 78% 45%, rgba(45,122,69,0.7), rgba(45,122,69,0) 70%),
      radial-gradient(ellipse 30% 12% at 55% 66%, rgba(214,196,160,0.55), rgba(214,196,160,0) 75%),
      linear-gradient(180deg, var(--sky-dark) 0%, var(--sky-mid) 35%, #2c5a40 55%, var(--grass) 70%, #8aa083 82%, var(--paper) 100%);
  }
  .headline {
    position: absolute;
    left: 0; top: 40px;
    width: 100%;
    text-align: center;
    color: var(--headline);
    font-family: "Oswald", sans-serif;
  }
  .headline-offer {
    display: block;
    font-weight: 200;
    font-size: 172px;
    line-height: 1;
    letter-spacing: 2px;
  }
  .headline-sub {
    display: block;
    margin-top: 18px;
    font-weight: 300;
    font-size: 46px;
    line-height: 1;
    letter-spacing: 0.32em;
    padding-left: 0.32em;
  }
  .offer-copy {
    position: absolute;
    left: 0; top: 712px;
    width: 100%;
    text-align: center;
    color: var(--ink);
    text-transform: uppercase;
  }
  .offer-intro {
    font-family: "Oswald", sans-serif;
    font-weight: 300;
    font-size: 34px;
    line-height: 38px;
  }
  .offer-brand {
    font-family: "Oswald", sans-serif;
    font-weight: 500;
    font-size: 44px;
    line-height: 50px;
    color: var(--brand-green);
    margin-bottom: 4px;
  }
  .offer-details {
    font-family: "Roboto Condensed", sans-serif;
    font-weight: 500;
    font-size: 27px;
    line-height: 33.6px;
    text-transform: none;
  }
  .call-to-action {
    position: absolute;
    left: 0; top: 1118px;
    width: 100%;
    text-align: center;
    font-family: "Oswald", sans-serif;
    font-weight: 500;
    font-size: 44px;
    line-height: 52px;
    color: var(--brand-green);
    text-transform: uppercase;
  }
</style>
</head>
<body>
  <main class="flyer">
    <div class="hero-scene" role="img" aria-label="Stormy dark green sky with a large green umbrella sheltering a two-storey house and a silver car on grass"></div>

    <h1 class="headline">
      <span class="headline-offer">50% OFF</span>
      <span class="headline-sub">COMMISSION</span>
    </h1>

    <section class="offer-copy">
      <p class="offer-intro">Sounds good doesn’t it?</p>
      <p class="offer-intro">Our promise to you from</p>
      <p class="offer-brand">Harlow Real Estate</p>
      <div class="offer-details">
        <p>List your property with us</p>
        <p>And if your buyer has not been found within 15 days</p>
        <p>We will slash 50% off our commission!</p>
        <p>You will have the benefit of Real Estate consultants</p>
        <p>Derek Harlow and Anthony Velluti</p>
        <p>With over 40 years combined experience</p>
        <p>Working hard to find your buyer.</p>
      </div>
    </section>

    <p class="call-to-action">Call today 0491 627 158</p>
  </main>
</body>
</html>
```